Tovell Family Law, legal technician needs a website and design

I need a website for a family law practice. I specialize in collaborative law, unbundled services, and mediation. The website must contain my company logo (file attached), and the website must be a mixture of my personality and my profession. I have attached additional information to explain my personality and profession.

Target Market(s)

Lower through middle-class (income level up to $200,000 per year)

Coding

Coded - Design and coding required

Number of Pages Required

1 page

Requirements
Must have
• Must have enough pages to cover required content. I submitted below some content about the collaborative law process. All of the content is not necessary. However, the website must have enough content to clearly describe the services I offer. Use your professionalism and judgment regarding font, font size, etc.

```html
<!DOCTYPE html>
<html lang="en">
<head>
<meta charset="utf-8">
<title>Tovell Family Law</title>
<link href="https://fonts.googleapis.com/css2?family=Cinzel:wght@400;600;700&family=Crimson+Text:wght@400;600&family=Lato:wght@400;700&display=swap" rel="stylesheet">
<style>
:root{
  --gold:#b9b53c;
  --gold-bright:#d8d24a;
  --gold-dark:#7a7820;
  --ink:#1c1b18;
  --dark:#171511;
  --text:#2b2a27;
  --muted:#6d6b66;
  --light:#efefef;
  --canvas:#f3f3f3;
  --white:#ffffff;
}
*{margin:0;padding:0;box-sizing:border-box}
html,body{width:1200px;height:4071px;overflow:hidden}
body{background:var(--canvas);font-family:"Crimson Text",Georgia,serif;color:var(--text)}
.page{position:absolute;left:186px;top:133px;width:814px;height:3671px;background:var(--white);box-shadow:0 10px 60px rgba(0,0,0,.22);overflow:visible}
section,header,footer{position:absolute;left:0;width:814px}
.abs{position:absolute}
.heading{font-family:"Cinzel",serif;font-weight:700;letter-spacing:.5px;color:var(--ink)}
.btn-solid{position:absolute;display:flex;align-items:center;justify-content:center;background:linear-gradient(180deg,#c9c54a,#8f8c22);color:#fff;font-size:10px;font-family:"Crimson Text",serif;border-radius:1px}
.btn-line{position:absolute;display:flex;align-items:center;justify-content:center;border:1.5px solid var(--gold);color:var(--gold-bright);font-size:11px}
.photo{position:absolute}

/* hero */
.hero{top:0;height:439px;background:linear-gradient(180deg,#2a2d35 0%,#3a3e47 35%,#24262b 70%,#1d1d1f 100%)}
.brand{position:absolute;left:42px;top:20px;display:flex;align-items:center;gap:8px;color:var(--gold);font-family:"Cinzel",serif;font-size:11px;font-weight:600}
.brand .mark{width:14px;height:14px;border:1.5px solid var(--gold)}
.nav{position:absolute;top:32px;left:0;width:814px;height:14px}
.nav a{position:absolute;color:var(--gold-bright);font-size:11px;text-decoration:none;font-family:"Crimson Text",serif;letter-spacing:.3px}
.nav-rule{position:absolute;left:0;top:63px;width:814px;height:1px;background:rgba(185,181,60,.45)}
.hero-title{position:absolute;top:196px;width:814px;text-align:center;font-family:"Cinzel",serif;font-weight:400;font-size:40px;color:#fff;letter-spacing:1px}
.hero-sub{position:absolute;top:248px;width:814px;text-align:center;color:var(--gold-bright);font-size:11.5px;line-height:15px}

/* about */
.about{top:439px;height:371px;background:#fff}
.ghost{position:absolute;left:56px;top:60px;font-family:"Cinzel",serif;font-weight:700;font-size:46px;color:#e5e5e5;letter-spacing:1px}
.about-title{position:absolute;left:83px;top:75px;font-size:29px}
.kicker{font-family:"Cinzel",serif;font-weight:600;font-size:12px;color:var(--ink)}
.body-copy{font-size:11.6px;line-height:14.6px;color:var(--text)}
.welcome{position:absolute;left:560px;top:211px;width:296px;text-align:center;font-family:"Cinzel",serif;font-size:18px;line-height:22px;color:var(--gold-bright)}

/* practice */
.practice{top:810px;height:278px;background:linear-gradient(180deg,#1b1814,#2a241c 50%,#15130f)}
.center{position:absolute;width:814px;text-align:center}
.rule{position:absolute;height:2px;background:var(--gold)}

/* why */
.why{top:1088px;height:1220px;background:var(--light)}
.why-title{top:62px;font-size:25px;line-height:32px}
.reason h3{position:absolute;font-family:"Cinzel",serif;font-weight:700;font-size:15px;color:var(--ink)}
.reason h3 span{border-bottom:2px solid var(--gold)}
.reason p{position:absolute;width:290px}

/* stats */
.stats{top:2308px;height:161px;background:linear-gradient(90deg,#141210,#2a251f 60%,#16130f)}

/* choose */
.choose{top:2469px;height:381px;background:#fff}

/* mediation */
.mediation{top:2850px;height:283px;background:linear-gradient(90deg,#151310,#221e18 55%,#332b22)}

/* fees */
.fees{top:3133px;height:400px;background:#fff}
.fees ul{position:absolute;left:356px;top:162px;list-style:none;width:380px}
.fees li{position:relative;padding-left:22px;font-size:11.6px;line-height:14.6px}
.fees li::before{content:"";position:absolute;left:4px;top:4px;width:6px;height:6px;border-radius:50%;background:var(--gold)}

/* footer */
.site-footer{top:3533px;height:271px;background:#1b1b1b;color:#fff}
.site-footer h4{position:absolute;font-family:"Cinzel",serif;font-weight:400;font-size:17px;color:#fff}
.links a{position:absolute;left:205px;font-family:"Cinzel",serif;font-size:11px;color:#fff;text-decoration:none}
.contact-item{position:absolute;left:363px;display:flex;gap:10px;font-size:11px;line-height:13px;color:#fff}
.field{position:absolute;background:#fff;color:#999;font-family:"Lato",sans-serif;font-size:7px;padding:3px 5px}
</style>
</head>
<body>
<div class="page">

  <header class="hero">
    <div class="photo" role="img" aria-label="City skyline with a tall needle tower under a cloudy dusk sky" style="left:0;top:0;width:814px;height:439px;background:linear-gradient(180deg,rgba(90,96,110,.55),rgba(30,30,34,.85))"></div>
    <div class="brand"><span class="mark"></span>Tovell Family Law</div>
    <nav class="nav">
      <a style="left:261px">HOME</a>
      <a style="left:333px">ABOUT US</a>
      <a style="left:420px">PRACTICE AREAS</a>
      <a style="left:542px">PROCESS</a>
      <a style="left:620px">MEDIATION</a>
      <a style="left:713px">CONTACT US</a>
    </nav>
    <div class="nav-rule"></div>
    <div class="photo" role="img" aria-label="Scales of justice emblem" style="left:380px;top:130px;width:54px;height:50px;background:linear-gradient(180deg,rgba(216,210,74,.0),rgba(216,210,74,.25));border-bottom:2px solid var(--gold)"></div>
    <h1 class="hero-title">TOVELL FAMILY LAW</h1>
    <p class="hero-sub">Lorem Ipsum Dolor Sit Amet Consectetur Adipiscing Elit Tellus Neque Feugiat Sit Justo, Nec Nisl, Sed.<br>Tristique Urna Tellus Erat Suscipit Vulputate Integer Vitae.</p>
    <div class="btn-line" style="left:345px;top:297px;width:128px;height:28px">View Practice Areas</div>
    <svg class="abs" style="left:400px;top:388px" width="14" height="22" viewBox="0 0 14 22"><path d="M7 1v19M2 15l5 5 5-5" stroke="#9a9a9a" stroke-width="1.4" fill="none"/></svg>
  </header>

  <section class="about">
    <div class="ghost">ABOUT US</div>
    <h2 class="heading about-title">ABOUT US</h2>
    <div class="abs kicker" style="left:83px;top:131px">WHAT IS COLLABORATIVE LAW?</div>
    <p class="abs body-copy" style="left:83px;top:150px;width:300px">Every Year, Hundreds Of Thousands Of Marriages End In Divorce. Are You In This Situation Right Now? Are You Getting Ready To Hire A Lawyer To Help You With Your Case?<br>If So, Before You Make A Decision On The Process You Are Choosing For Your Divorce Process, Read On To Learn More About The Collaborative Approach To Divorce And You Will Discover The Benefits This Process Offers. When You Are Done Reading This Post You Will See Why So Many Divorcing Couples Choose The Collaborative Process For Their Divorce.</p>
    <div class="photo" role="img" aria-label="Two lawyers in suits reviewing documents at a desk" style="left:447px;top:0;width:367px;height:371px;background:linear-gradient(135deg,#3b3f47,#1e2025 60%,#2c2a24)"></div>
    <div class="photo" role="img" aria-label="Scales of justice emblem" style="left:686px;top:140px;width:44px;height:46px;border-bottom:2px solid var(--gold)"></div>
    <div class="welcome">WELLCOME TO<br>COLLABORATIVE<br>LAW?</div>
  </section>

  <section class="practice">
    <div class="photo" role="img" aria-label="Dim courtroom interior with wooden benches" style="left:0;top:0;width:814px;height:278px;background:radial-gradient(ellipse at 50% 70%,rgba(120,95,60,.35),rgba(0,0,0,0) 70%)"></div>
    <h2 class="center heading" style="top:52px;font-size:28px;color:#fff">PRACTICE</h2>
    <div class="rule" style="left:387px;top:92px;width:40px"></div>
    <div class="center kicker" style="top:99px;color:#fff;font-size:14px;font-weight:400">WHAT IS COLLABORATIVE PRACTICE?</div>
    <p class="abs body-copy" style="left:120px;top:124px;width:574px;text-align:center;color:#fff">Collaborate Practice Is A Process Where Trained Professionals, Including Attorneys, Help Couples Resolve Their Disputes Without Litigation And Outside Of Court. Instead, Those Involved In The Case Approach The Legal Process Through The Lens Of Teamwork, Trouble-Shooting, And Problem-Solving Rather Than Fighting To “Beat” Someone Else. Another Way Of Describing This Process Is Rather Than Looking At A “Win – Lose” Result, See It As A “Win-Win” For All Involved.</p>
    <div class="btn-line" style="left:367px;top:215px;width:78px;height:24px;font-size:10px">Learn More</div>
  </section>

  <section class="why">
    <h2 class="center heading why-title">WHY DO PEOPLE CHOOSE A<br>COLLABORATIVE DIVORCE PROCESS?</h2>
    <div class="rule" style="left:345px;top:131px;width:125px"></div>
    <p class="abs body-copy" style="left:120px;top:142px;width:574px;text-align:center">There Are Lots Of Reasons Why People Choose The Collaborative Process And Hire A Collaborative Attorney To Assist Them, Including The Following:</p>

    <div class="reason">
      <div class="photo" role="img" aria-label="Mother hugging her young daughter at home" style="left:134px;top:257px;width:199px;height:199px;background:linear-gradient(135deg,#d9cfc4,#b7a898 60%,#8d7d70)"></div>
      <h3 style="left:389px;top:266px"><span>CHIL</span>DREN FIRST</h3>
      <p class="body-copy" style="left:389px;top:292px">How Many Times Have You Talked To Someone Who Is A Child Of A Contentious Divorce, Or Seen A Friend Or Family Member Going Through A Divorce And Their Children Suffer As A Result Of The Acrimony? One Time Is Too Many. The Collaborative Process Puts The Children First, Working With The Parents To Not Put The Children</p>
      <div class="btn-solid" style="left:388px;top:411px;width:94px;height:26px">Learn More</div>
    </div>

    <div class="reason">
      <h3 style="left:134px;top:496px"><span>PRIV</span>ACY AND CONFIDENTIALITY</h3>
      <p class="body-copy" style="left:134px;top:522px">How Many Times Have You Talked To Someone Who Is A Child Of A Contentious Divorce, Or Seen A Friend Or Family Member Going Through A Divorce And Their Children Suffer As A Result Of The Acrimony? One Time Is Too Many. The Collaborative Process Puts The Children First, Working With The Parents To Not Put The Children</p>
      <div class="btn-solid" style="left:134px;top:640px;width:94px;height:26px">Learn More</div>
      <div class="photo" role="img" aria-label="Wooden judge's gavel with brass band" style="left:486px;top:467px;width:198px;height:199px;background:linear-gradient(135deg,#4a2c1c,#2a170e 60%,#6b4430)"></div>
    </div>

    <div class="reason">
      <div class="photo" role="img" aria-label="Brass scales and gavel on a desk" style="left:134px;top:715px;width:199px;height:199px;background:linear-gradient(135deg,#a88a6e,#6a4c38 60%,#3a2619)"></div>
      <h3 style="left:389px;top:728px"><span>INCR</span>EASED EFFICIENCY</h3>
      <p class="body-copy" style="left:389px;top:755px">How Many Times Have You Talked To Someone Who Is A Child Of A Contentious Divorce, Or Seen A Friend Or Family Member Going Through A Divorce And Their Children Suffer As A Result Of The Acrimony? One Time Is Too Many. The Collaborative Process Puts The Children First, Working With The Parents To Not Put The Children</p>
      <div class="btn-solid" style="left:388px;top:878px;width:94px;height:26px">Learn More</div>
    </div>

    <div class="reason">
      <h3 style="left:134px;top:978px"><span>LOWE</span>R COSTS/ HIGHER REWARDS</h3>
      <p class="body-copy" style="left:134px;top:1005px">How Many Times Have You Talked To Someone Who Is A Child Of A Contentious Divorce, Or Seen A Friend Or Family Member Going Through A Divorce And Their Children Suffer As A Result Of The Acrimony? One Time Is Too Many. The Collaborative Process Puts The Children First, Working With The Parents To Not Put The Children</p>
      <div class="btn-solid" style="left:134px;top:1127px;width:94px;height:26px">Learn More</div>
      <div class="photo" role="img" aria-label="Gavel resting on a stack of banknotes" style="left:486px;top:944px;width:198px;height:199px;background:linear-gradient(135deg,#cfc8c4,#8a7d70 55%,#4a3a30)"></div>
    </div>
  </section>

  <section class="stats">
    <h2 class="center heading" style="top:30px;font-size:26px;color:#fff;font-weight:600">20 YEARS OF EXPERIENCE IN VARIOUS CASES</h2>
    <p class="abs body-copy" style="left:120px;top:69px;width:574px;text-align:center;color:#fff">Lorem Ipsum Dolor Sit Amet, Consectetur Adipiscing Elit. Sit Venenatis Molestie Sit Cras. Scelerisque Massa Feugiat Tempor Eget Enim Vitae Amet. Viverra Neque, Amet, Consectetur</p>
    <div class="abs" style="left:327px;top:120px;display:flex;align-items:center;gap:14px;font-family:'Cinzel',serif;font-size:16px;color:#fff">GET STARTED
      <svg width="26" height="10" viewBox="0 0 26 10"><path d="M0 5h24M19 1l5 4-5 4" stroke="#fff" stroke-width="1.3" fill="none"/></svg>
    </div>
  </section>

  <section class="choose">
    <div class="photo" role="img" aria-label="Lawyer signing papers beside a gavel and scales" style="left:80px;top:57px;width:258px;height:256px;background:linear-gradient(135deg,#3c3e44,#1f2024 60%,#2e2b24)"></div>
    <div class="abs" style="left:93px;top:70px;width:232px;height:230px;border:1.5px solid var(--gold)"></div>
    <h2 class="abs heading" style="left:398px;top:100px;font-size:25px;line-height:33px">CHOOSE COLLABORATIVE<br>DIVORCE</h2>
    <p class="abs body-copy" style="left:398px;top:180px;width:310px">As You Can See, There Are Plenty Of Reasons To Consider Collaborative Practice. It Will Help You To Peacefully Resolve Conflicts And Move Through The Legal Process As Efficiently And Cost-Effectively As Possible.<br>Want To Learn More About Collaborative Practice? Contact Tovell Family Law.</p>
  </section>

  <section class="mediation">
    <h2 class="abs heading" style="left:80px;top:46px;font-size:26px;color:#fff;font-weight:600">MEDIATION</h2>
    <div class="rule" style="left:80px;top:84px;width:52px"></div>
    <p class="abs body-copy" style="left:80px;top:94px;width:440px;color:#fff">Mediation To Help You Reach An Agreement $250 Per Hour, Available.</p>
    <p class="abs body-copy" style="left:80px;top:124px;width:440px;color:#fff">In Addition To The Above Packages, We Offer The Following Services, Which Can Be Adapted To Your Individual Situation:</p>
    <p class="abs body-copy" style="left:80px;top:169px;width:440px;color:#fff">&nbsp;If You Both Agree And You Have Already Filled Out Your Own Divorce Forms - Divorce Form Review $150 Flat Fee For A One-Time Review, Research, And Recommendations</p>
    <div class="btn-solid" style="left:80px;top:226px;width:92px;height:26px">View More</div>
    <div class="photo" role="img" aria-label="Smiling lawyer in white shirt and tie with arms crossed" style="left:561px;top:-79px;width:211px;height:362px;background:linear-gradient(180deg,#e8ecf3,#c8d2e0 55%,#8e9bb0);border-radius:90px 90px 0 0"></div>
  </section>

  <section class="fees">
    <div class="photo" role="img" aria-label="Couple meeting with a mediator at a table" style="left:64px;top:71px;width:258px;height:272px;background:linear-gradient(135deg,#c9c7c3,#7a7570 55%,#2e2c2a)"></div>
    <h2 class="abs heading" style="left:356px;top:84px;font-size:25px;line-height:32px">DIVORCE WITHOUT COURT<br>SERVICES AND FEES</h2>
    <ul>
      <li style="margin-bottom:14px">You've Talked And You Both Agree On Exactly What You Want To Do With Your Assets</li>
      <li style="margin-bottom:15px">There Is No Need For Mediation</li>
      <li style="margin-bottom:17px">You Have No Children, Or Your Children Are Older Than 18: Settlement Agreement Is For Tax Purposes Only</li>
      <li>Never Go To Court</li>
    </ul>
    <div class="abs body-copy" style="left:356px;top:308px;text-decoration:underline">$899, Plus Court Filing Fees</div>
    <svg class="abs" style="left:680px;top:329px" width="52" height="12" viewBox="0 0 52 12"><path d="M20 6H2M6 2L2 6l4 4" stroke="#b9b53c" stroke-width="1.5" fill="none"/><path d="M32 6h18M46 2l4 4-4 4" stroke="#b9b53c" stroke-width="1.5" fill="none"/></svg>
  </section>

  <footer class="site-footer">
    <div class="abs" style="left:42px;top:60px;display:flex;align-items:center;gap:7px;font-family:'Cinzel',serif;font-size:12px;color:#fff">
      <span style="width:14px;height:14px;border:1.5px solid #fff;border-radius:50%"></span>Tovell Family Law</div>
    <p class="abs" style="left:42px;top:126px;width:140px;font-size:8px;line-height:10px;color:#fff">As You Can See, There Are Plenty Of Reasons To Consider Collaborative Practice.</p>

    <h4 style="left:203px;top:52px">QUICK LINKS</h4>
    <div class="links">
      <a style="top:89px">HOME</a>
      <a style="top:110px">ABOUT US</a>
      <a style="top:131px">PRACTICE AREAS</a>
      <a style="top:153px">PROCESS</a>
      <a style="top:174px">MEDIATION</a>
      <a style="top:195px">CONTACT US</a>
    </div>

    <h4 style="left:363px;top:52px">CONTACT US</h4>
    <div class="contact-item" style="top:85px">
      <svg width="10" height="10" viewBox="0 0 10 10"><path d="M2 1l2 2-1 1.5c.6 1.2 1.4 2 2.5 2.5L7 6l2 2-1.5 1.5C4.5 9 1 5.5.5 2.5z" fill="#b9b53c"/></svg>6644-5120-39</div>
    <div class="contact-item" style="top:109px">
      <svg width="10" height="10" viewBox="0 0 10 10"><rect x=".5" y="1.5" width="9" height="7" fill="none" stroke="#b9b53c"/><path d="M.5 1.5l4.5 4 4.5-4" fill="none" stroke="#b9b53c"/></svg>hello@tovellfamilylaw.com</div>
    <div class="contact-item" style="top:132px">
      <svg width="10" height="10" viewBox="0 0 10 10"><path d="M9 1L1 4.5l3.5 1L5.5 9z" fill="#b9b53c"/></svg>Maple Court 18 near Elm Plaza,<br>Riverton</div>

    <h4 style="left:545px;top:50px">GET IN TOUCH</h4>
    <div class="field" style="left:545px;top:77px;width:110px;height:19px">Name</div>
    <div class="field" style="left:665px;top:77px;width:108px;height:19px">Phone number</div>
    <div class="field" style="left:545px;top:104px;width:110px;height:19px">Subject</div>
    <div class="field" style="left:665px;top:104px;width:108px;height:19px">Email</div>
    <div class="field" style="left:545px;top:133px;width:228px;height:39px">Message</div>
    <div class="btn-solid" style="left:545px;top:186px;width:77px;height:19px;border-radius:10px;font-family:'Lato',sans-serif;font-size:7px">SUBMIT</div>

    <div class="abs" style="left:98px;top:245px;width:618px;height:1px;background:#555"></div>
    <div class="center" style="top:253px;font-family:'Lato',sans-serif;font-size:7px;color:#ddd">COPYRIGHTS © 2021 TOVELL FAMILY LAW. ALL RIGHTS RESERVED. TERMS &amp; CONDITIONS</div>
  </footer>

</div>
</body>
</html>
```